VORLA:advise Business Cards

We need a business card design for VORLA:advise (Logo Attached), a management consultancy specialized in brand & business building.

Design should be clean, smart and a touch of innnovation without being gimmicky.

The details on the card should be:
Name: Tomas Vellaquin
Title: Managing Director
Address: 42 Marden Wharf, Kestrel Tower Building, Singapore 073296
Tel: +6284729156048
email: tv@vorlaadvise.example
website: vorlaadvise.example

For further background on corporate identity, please check www.vorlaadvise.example
Updates

Dear all,

Many thanks for the submissions so far! I gave feedback to those designs that I prefer at this stage.

Overall I see that my preference goes into the direction that 'less is more' and 'simple is beautiful'

Please create uniqueness and standout by the simplicity and attraction of the overall concept and design.

Many thanks and please shout incase of questions!

Tomas

Industry/Entity Type

Business

```html
<!DOCTYPE html>
<html lang="en">
<head>
<meta charset="utf-8">
<title>Vorla Partners Business Cards</title>
<link href="https://fonts.googleapis.com/css2?family=Open+Sans:wght@400;600;700&display=swap" rel="stylesheet">
<style>
  :root {
    --stage: #3b2619;
    --paper: #ffffff;
    --orange: #ff6600;
    --charcoal: #4b4b4b;
    --ink: #3f3f3f;
    --rule: #555555;
    --label: #f2f2f2;
  }
  * { margin: 0; padding: 0; box-sizing: border-box; }
  html, body { width: 1200px; height: 766px; overflow: hidden; }
  body {
    position: relative;
    background: var(--stage);
    font-family: "Open Sans", Arial, sans-serif;
  }
  .card { position: absolute; width: 569px; height: 324px; }

  /* Front */
  .card-front {
    left: 260px; top: 22px;
    background: var(--paper);
    border: 1px solid #222;
  }
  .front-logo {
    position: absolute; left: 0; right: 0; top: 52px;
    text-align: center;
    font-size: 36px; font-weight: 600; letter-spacing: 0.5px; line-height: 48px;
    color: var(--charcoal);
  }
  .divider {
    position: absolute; top: 174px; height: 2px; background: var(--rule);
  }
  .divider-left { left: 0; width: 197px; }
  .divider-right { right: 0; width: 198px; }
  .identity {
    position: absolute; left: 0; right: 0; top: 152px; text-align: center;
  }
  .person-name { font-size: 17px; font-weight: 700; color: var(--ink); line-height: 24px; }
  .person-title { font-size: 13px; font-weight: 600; color: var(--orange); line-height: 18px; }
  .contact {
    position: absolute; left: 0; right: 0; top: 236px;
    text-align: center; font-size: 13.5px; color: var(--ink); line-height: 23px;
  }
  .contact-line { display: flex; justify-content: center; align-items: center; gap: 4px; }
  .contact-line .gap { width: 6px; }
  .icon { width: 12px; height: 12px; fill: none; stroke: var(--ink); stroke-width: 1.4; }
  .address { margin-top: 4px; }

  /* Backs */
  .card-back { top: 379px; }
  .back-orange { left: 23px; background: var(--orange); }
  .back-grey { left: 616px; background: var(--charcoal); }
  .back-logo {
    position: absolute; left: 0; right: 0; top: 98px;
    text-align: center; color: var(--paper);
    font-size: 60px; font-weight: 600; letter-spacing: 1px; line-height: 80px;
  }
  .back-url {
    position: absolute; left: 0; right: 0; top: 222px;
    text-align: center; color: var(--paper);
    font-size: 16px; font-weight: 600; letter-spacing: 3.2px;
  }
  .card-label {
    position: absolute; top: 722px; width: 200px;
    text-align: center; color: var(--label); font-size: 22px;
  }
  .label-back-1 { left: 199px; }
  .label-back-2 { left: 820px; }
</style>
</head>
<body>
  <section class="card card-front">
    <div class="front-logo">vorla partners</div>
    <div class="divider divider-left"></div>
    <div class="divider divider-right"></div>
    <div class="identity">
      <div class="person-name">Tomas Vellaquin</div>
      <div class="person-title">Managing Director</div>
    </div>
    <div class="contact">
      <div class="contact-line">
        <svg class="icon" viewBox="0 0 12 12" aria-hidden="true"><circle cx="6" cy="6" r="5.2"/><path d="M4 3.5l1 1.3-.6.8a4 4 0 0 0 2 2l.8-.6 1.3 1-.6.9c-2.2-.2-4-2-4.3-4.3z"/></svg>
        <span>+6284729156048</span>
      </div>
      <div class="contact-line">
        <svg class="icon" viewBox="0 0 12 12" aria-hidden="true"><rect x="1" y="3" width="10" height="7"/><path d="M1 3l5 4 5-4"/></svg>
        <span>tv@vorlaadvise.example</span>
        <span class="gap"></span>
        <svg class="icon" viewBox="0 0 12 12" aria-hidden="true"><circle cx="6" cy="6" r="5"/><ellipse cx="6" cy="6" rx="2.2" ry="5"/><path d="M1 6h10"/></svg>
        <span>www.vorlaadvise.example</span>
      </div>
      <div class="address">42 Marden Wharf, Kestrel Tower Building, Singapore 073296</div>
    </div>
  </section>

  <section class="card card-back back-orange">
    <div class="back-logo">vorla partners</div>
    <div class="back-url">www.vorlaadvise.example</div>
  </section>

  <section class="card card-back back-grey">
    <div class="back-logo">vorla partners</div>
    <div class="back-url">www.vorlaadvise.example</div>
  </section>

  <div class="card-label label-back-1">Back-1</div>
  <div class="card-label label-back-2">Back-2</div>
</body>
</html>
```